Design a modern, classy & professional business card for an online real estate agency, specializing in medium-luxury properties in Thailand and later in Singapore and UK.

Possible design ideas so far: (not essential)

- curved corner(s) to the card, white on front & turquoise on back or visa versa.

- front of card - clear and simple, company name in metallic grey/monochrome, logo graphic & company name on front in spot UV or embossed/debossed effect.

- back of card - large, close-cropped, 'ghost' patterns of the C-shaped curves of logo, or company name repeated on back of card in spot UV.

Target Market(s)

- young to middle-aged professionals mainly (but ideally should design should suit all)

- UK, US,EU,AUS & ASIAN mainly (but ideally should design should suit all countries)

Industry/Entity Type

Real Estate

Requirements
Must have
• THEME:
- Luxurious & Modern
- Clean & striking
- Unique & creative

INFO:
- Logo & company name on front
- Contact details on back:

Tobias Lindqvar
Managing Director

www.velmoraestates.example
www.velmoraestates-uk.example

Tel: 084-273-6190
email: tobias@velmoraestates.example

(contact details can be displayed in any order as suites design.)

Nice to have
• - curved corner(s) to the card, white on front & turquoise on back or visa versa.

Should not have
• - No generic images of properties, palm trees/coconut trees etc.

- No other other bold colors, except for main turquoise, grey, metallic white & black theme.

- No obvious business card templates

```html
<!DOCTYPE html>
<html lang="en">
<head>
<meta charset="utf-8">
<title>Velmora Estates – Business Card</title>
<link rel="stylesheet" href="https://fonts.googleapis.com/css2?family=Arimo:wght@400;700&display=swap">
<style>
  :root {
    --backdrop: #c3cfcf;
    --backdrop-light: #d4dddd;
    --card-white: #ffffff;
    --turquoise: #6cf0c2;
    --turquoise-deep: #5fe2b4;
    --slate-grey: #6f7a7c;
    --ink: #3a3f41;
    --soft-white: #f4fffb;
  }
  * { box-sizing: border-box; margin: 0; padding: 0; }
  html, body {
    width: 1200px;
    height: 726px;
    overflow: hidden;
  }
  body {
    background: radial-gradient(ellipse at 40% 35%, var(--backdrop-light), var(--backdrop));
    font-family: "Arimo", Arial, sans-serif;
    position: relative;
  }
  .card {
    position: absolute;
    top: 220px;
    width: 500px;
    height: 286px;
    border-radius: 22px;
    box-shadow: 0 14px 30px rgba(60, 80, 80, 0.22);
    overflow: hidden;
  }
  .card--front { left: 70px; background: var(--card-white); }
  .card--back  { left: 630px; background: linear-gradient(160deg, var(--turquoise), var(--turquoise-deep)); }

  .holder {
    position: absolute;
    top: 30px;
    right: 34px;
    text-align: right;
  }
  .holder__name {
    font-size: 22px;
    letter-spacing: 0.3px;
  }
  .holder__role {
    font-size: 10px;
    margin-top: 3px;
  }
  .card--front .holder__name,
  .card--front .holder__role { color: var(--ink); }
  .card--back .holder__name { color: var(--ink); font-weight: 700; }
  .card--back .holder__role { color: var(--ink); }

  .brand {
    position: absolute;
    left: 34px;
    bottom: 46px;
    display: flex;
    align-items: center;
    gap: 20px;
  }
  .brand__square {
    width: 108px;
    height: 108px;
    background: var(--turquoise);
  }
  .brand__name {
    color: var(--slate-grey);
    font-weight: 400;
    line-height: 1;
  }
  .brand__name-main {
    display: block;
    font-size: 58px;
    letter-spacing: -1px;
  }
  .brand__name-sub {
    display: block;
    font-size: 19px;
    letter-spacing: 9px;
    margin-top: 6px;
    padding-left: 4px;
  }

  .contacts {
    position: absolute;
    left: 32px;
    bottom: 30px;
    list-style: none;
    color: var(--soft-white);
    font-size: 13px;
    line-height: 20px;
  }
  .contacts li { display: flex; align-items: center; gap: 8px; }
  .contacts svg { width: 12px; height: 12px; flex: none; }
</style>
</head>
<body>

  <section class="card card--front" aria-label="Card front">
    <div class="holder">
      <p class="holder__name">Tobias Lindqvar</p>
      <p class="holder__role">Managing Director</p>
    </div>
    <div class="brand">
      <div class="brand__square"></div>
      <p class="brand__name">
        <span class="brand__name-main">Velmora</span>
        <span class="brand__name-sub">ESTATES</span>
      </p>
    </div>
  </section>

  <section class="card card--back" aria-label="Card back">
    <div class="holder">
      <p class="holder__name">Tobias Lindqvar</p>
      <p class="holder__role">Managing Director</p>
    </div>
    <ul class="contacts">
      <li>
        <svg viewBox="0 0 12 12" aria-hidden="true"><circle cx="6" cy="6" r="5" fill="none" stroke="#3a3f41" stroke-width="1.2"/><path d="M1 6h10M6 1c-2.5 3-2.5 7 0 10M6 1c2.5 3 2.5 7 0 10" fill="none" stroke="#3a3f41" stroke-width="1"/></svg>
        www.velmoraestates.example
      </li>
      <li>
        <svg viewBox="0 0 12 12" aria-hidden="true"><circle cx="6" cy="6" r="5" fill="none" stroke="#3a3f41" stroke-width="1.2"/><path d="M1 6h10M6 1c-2.5 3-2.5 7 0 10M6 1c2.5 3 2.5 7 0 10" fill="none" stroke="#3a3f41" stroke-width="1"/></svg>
        www.velmoraestates-uk.example
      </li>
      <li>
        <svg viewBox="0 0 12 12" aria-hidden="true"><rect x="1" y="5" width="10" height="6" rx="1" fill="#3a3f41"/><path d="M1 4c0-3 10-3 10 0" fill="none" stroke="#3a3f41" stroke-width="1.6"/></svg>
        Tel: 084-273-6190
      </li>
      <li>
        <svg viewBox="0 0 12 12" aria-hidden="true"><rect x="1" y="2.5" width="10" height="7" fill="none" stroke="#3a3f41" stroke-width="1.2"/><path d="M1 2.5l5 4 5-4" fill="none" stroke="#3a3f41" stroke-width="1.2"/></svg>
        email: tobias@velmoraestates.example
      </li>
    </ul>
  </section>

</body>
</html>
```